創業130年以上の酢屋です。
国産のりんご果汁だけから造られた「澄実の雫」のラベルデザインを依頼します。
一般のスーパーに卸す商品です。たくさん並ぶ大手さんの「りんご酢」に埋もれない、目を引くデザインをお願いしたいです。
容器は瓶で、スタイリッシュなものではなくごく普通の透明な瓶。お酢は薄い琥珀色です(現在のデザインは画像参照)
国産のりんご果汁100%でできているという点がセールスポイントです。
ターゲットは30代以上の女性。
用途はドレッシング作りやマリネなどの料理、フルーツビネガー等のドリンク作りなどです。
「清潔感」「素朴さ」「丁寧な日常」「かわいらしさ」等、30代以上の女性が好むイメージでデザインしてもらいたいです。

縦に並んだりんごのデザインが大変かわいらしく、中央の商品名、その両脇にあるセールスポイントの文言もはっきりと目立っていました。チラッと見ただけでも印象に残り、年配の方でもはっきり読める大きな文字は、20代~50代のどの従業員さんにも好評でした。手に取ってみると、りんごの中に使用方法や弊社の創業年もあり、お客様に伝えた情報がコンパクトにつまっいてる点も採用のポイントとなりました。

初めて利用しましたが、たくさんのデザイナー様にご提案いただき、感激いたしました。
様々なタイプのデザインの中から選ぶことができたので、これまでのモヤモヤ(本当はこれだ!と思ってないけど、選択肢が二択程度しかなくて、どちらかを選ばざるを得ない)が無く、100%納得の決定ができました。
この後、新商品もすぐに出す予定なのでまた利用したいと思っています。
ご応募いただいた皆様、ほんとうにありがとうございました。
またご縁がありましたら、どうぞよろしくお願い致します。
柏木喜三郎商店(有)
担当:岡部

```html
<!DOCTYPE html>
<html lang="ja">
<head>
<meta charset="utf-8">
<title>りんご酢 ラベル</title>
<link rel="stylesheet" href="https://fonts.googleapis.com/css2?family=Noto+Serif+JP:wght@300;400&family=Noto+Sans+JP:wght@400;500&display=swap">
<style>
  :root {
    --canvas: #f3f1ed;
    --label: #ffffff;
    --band: #f2aaa2;
    --apple: #e9685e;
    --ink: #3a3a3a;
    --accent: #ea6f66;
  }
  * { margin: 0; padding: 0; box-sizing: border-box; }
  html, body { width: 858px; height: 1200px; overflow: hidden; }
  body {
    background: var(--canvas);
    position: relative;
    font-family: "Noto Sans JP", sans-serif;
    color: var(--ink);
  }
  .label {
    position: absolute;
    left: 79px; top: 240px;
    width: 700px; height: 720px;
    background: var(--label);
    box-shadow: 0 2px 12px rgba(0,0,0,0.06);
  }
  .band {
    position: absolute; left: 0; width: 100%;
    background: var(--band);
  }
  .band--top {
    top: 24px; height: 68px;
    display: flex; align-items: center; justify-content: center; gap: 14px;
  }
  .band--bottom { bottom: 40px; height: 68px; }
  .maker-mark { width: 40px; height: 40px; background: var(--label); flex: none; }
  .maker-name {
    color: var(--label); font-size: 20px; font-weight: 500;
    letter-spacing: 0.2em; line-height: 1;
  }
  .product-name {
    position: absolute; top: 200px; width: 100%; text-align: center;
    font-family: "Noto Serif JP", serif; font-weight: 300;
    font-size: 62px; letter-spacing: 0.42em; padding-left: 0.42em;
    line-height: 1.2;
  }
  .product-kana {
    position: absolute; top: 292px; width: 100%; text-align: center;
    font-family: "Noto Serif JP", serif; font-weight: 400;
    font-size: 28px; letter-spacing: 0.28em; padding-left: 0.28em;
    line-height: 1.2;
  }
  .apple-art {
    position: absolute; top: 380px; left: 50%; margin-left: -34px;
    width: 68px; height: 72px;
  }
  .selling-point {
    position: absolute; top: 500px; width: 100%;
    display: flex; justify-content: center; align-items: center; gap: 40px;
    font-size: 26px; letter-spacing: 0.12em; line-height: 1.3;
  }
  .selling-point em { font-style: normal; color: var(--accent); }
  .category-badge {
    border: 1.5px solid var(--ink);
    font-size: 15px; padding: 2px 8px; letter-spacing: 0.05em;
  }
</style>
</head>
<body>
  <main class="label">
    <div class="band band--top">
      <span class="maker-mark"></span>
      <span class="maker-name">澄川酢店</span>
    </div>

    <h1 class="product-name">RINGOSU</h1>
    <p class="product-kana">りんご酢</p>

    <svg class="apple-art" viewBox="0 0 68 72" role="img" aria-label="りんごのイラスト">
      <circle cx="34" cy="40" r="31" fill="var(--apple)"/>
    </svg>

    <div class="selling-point">
      <p>国内産<em>りんご果汁</em>使用</p>
      <span class="category-badge">醸造酢</span>
    </div>

    <div class="band band--bottom"></div>
  </main>
</body>
</html>
```